Startup Drone Platform Company business card

We are needing a business card design for our employees. We are a startup drone platform. We are looking for a business card that has our logo on one side, with the employee/company details on the opposite side. We are looking for something that is very eye catching, modern, and bold.

Target Market(s)

This will target both drone pilots and drone businesses, along with all the industries that could utilize drone services (aerial video, aerial photos, inspections, 3d mapping, etc).

Industry/Entity Type

Business

```html
<!DOCTYPE html>
<html lang="en">
<head>
<meta charset="utf-8">
<title>Skyward Lift – Business Card</title>
<link rel="stylesheet" href="https://fonts.googleapis.com/css2?family=Lato:wght@400;700;900&display=swap">
<style>
  :root {
    --canvas-bg: #ecebe8;
    --card-dark: #2b2b2e;
    --card-white: #ffffff;
    --brand-blue: #1b64bd;
    --brand-teal: #3cb8c6;
    --text-light: #f2f2f2;
    --text-muted: #d4d4d6;
  }
  * { box-sizing: border-box; margin: 0; padding: 0; }
  html, body { width: 1200px; height: 891px; overflow: hidden; }
  body {
    background: var(--canvas-bg);
    font-family: "Lato", Arial, sans-serif;
    position: relative;
  }
  .card {
    position: absolute;
    top: 291px;
    width: 540px;
    height: 309px;
    border-radius: 6px;
    overflow: hidden;
    box-shadow: 0 10px 28px rgba(0,0,0,0.18);
    background: var(--card-dark);
  }
  .card--back { left: 40px; }
  .card--front { left: 620px; }

  /* back side: brand name */
  .back-brand {
    position: absolute;
    inset: 0;
    display: flex;
    flex-direction: column;
    align-items: center;
    justify-content: center;
    gap: 22px;
  }
  .back-brand__mark {
    width: 46px; height: 46px;
    border: 3px solid var(--text-light);
    border-radius: 50%;
  }
  .back-brand__name {
    color: var(--text-light);
    font-weight: 700;
    font-size: 30px;
    letter-spacing: 10px;
    padding-left: 10px;
  }

  /* front side */
  .front-shapes { position: absolute; inset: 0; width: 540px; height: 309px; }
  .holder { position: absolute; left: 40px; top: 34px; color: var(--text-light); }
  .holder__name { font-weight: 900; font-size: 21px; letter-spacing: 0.5px; }
  .holder__title { color: var(--brand-teal); font-size: 11px; letter-spacing: 1px; margin-top: 1px; }
  .contact-list { position: absolute; left: 40px; top: 112px; list-style: none; }
  .contact-list li {
    display: flex; align-items: center; gap: 14px;
    color: var(--text-light); font-size: 12.5px; letter-spacing: 0.8px;
    height: 21px;
  }
  .contact-list svg { width: 13px; height: 13px; flex: none; }
  .front-brand {
    position: absolute; left: 360px; top: 118px; width: 150px;
    display: flex; align-items: center; justify-content: center; gap: 8px;
  }
  .front-brand__mark { width: 14px; height: 14px; border: 2px solid var(--card-dark); border-radius: 50%; }
  .front-brand__name {
    color: var(--card-dark); font-weight: 700; font-size: 14px; letter-spacing: 3px;
  }
  .address {
    position: absolute; right: 44px; bottom: 28px;
    display: flex; gap: 10px; color: var(--text-light);
    font-size: 12px; line-height: 1.3;
  }
  .address svg { width: 12px; height: 14px; margin-top: 1px; }
</style>
</head>
<body>

<section class="card card--back" aria-label="Card back">
  <div class="back-brand">
    <span class="back-brand__mark"></span>
    <span class="back-brand__name">SKYWARD LIFT</span>
  </div>
</section>

<section class="card card--front" aria-label="Card front">
  <svg class="front-shapes" viewBox="0 0 540 309" aria-hidden="true">
    <path d="M300 0 C410 10 360 230 120 309 L540 309 L540 0 Z" fill="var(--brand-blue)"/>
    <path d="M330 42 C420 34 500 30 540 30 L540 212 C420 210 300 245 190 300 C330 240 390 140 330 42 Z" fill="var(--card-white)"/>
    <path d="M330 42 C420 34 500 30 540 30" fill="none" stroke="var(--card-dark)" stroke-width="4"/>
    <path d="M540 212 C420 210 300 245 190 300" fill="none" stroke="var(--card-dark)" stroke-width="5"/>
  </svg>

  <div class="holder">
    <div class="holder__name">MARK DALTON</div>
    <div class="holder__title">DIRECTOR</div>
  </div>

  <ul class="contact-list">
    <li>
      <svg viewBox="0 0 14 14"><rect x="3.5" y="1" width="7" height="12" rx="1.2" fill="none" stroke="currentColor" stroke-width="1.2"/></svg>
      000.5550.1290
    </li>
    <li>
      <svg viewBox="0 0 14 14"><path d="M3 1.5 L5.5 4 L4.3 5.6 C5 7.5 6.5 9 8.4 9.7 L10 8.5 L12.5 11 L11 12.5 C6 12 2 8 1.5 3 Z" fill="none" stroke="currentColor" stroke-width="1.1" stroke-linejoin="round"/></svg>
      000.5550.1290
    </li>
    <li>
      <svg viewBox="0 0 14 14"><rect x="1" y="3" width="12" height="8" fill="none" stroke="currentColor" stroke-width="1.1"/><path d="M1 3 L7 8 L13 3" fill="none" stroke="currentColor" stroke-width="1.1"/></svg>
      hello@skywardlift.co
    </li>
    <li>
      <svg viewBox="0 0 14 14"><circle cx="7" cy="7" r="5.8" fill="none" stroke="currentColor" stroke-width="1.1"/><ellipse cx="7" cy="7" rx="2.5" ry="5.8" fill="none" stroke="currentColor" stroke-width="1"/><path d="M1.2 7 H12.8" stroke="currentColor" stroke-width="1"/></svg>
      www.skywardlift.co
    </li>
  </ul>

  <div class="front-brand">
    <span class="front-brand__mark"></span>
    <span class="front-brand__name">SKYWARD LIFT</span>
  </div>

  <div class="address">
    <svg viewBox="0 0 12 14"><path d="M6 13 C2 8.5 1 6.8 1 5 A5 5 0 0 1 11 5 C11 6.8 10 8.5 6 13 Z" fill="none" stroke="currentColor" stroke-width="1.1"/><circle cx="6" cy="5" r="1.6" fill="none" stroke="currentColor" stroke-width="1"/></svg>
    <div>14 ORCHID PLAZA<br>Harbor City, NORLAND</div>
  </div>
</section>

</body>
</html>
```